New Website for ReBranded Company - CrewBeacon

We have a successful company and website currently but it is a little dated. We have re-branded the company from Harbor Signal Networks to CrewBeacon and have a new logo for the new name. We are looking to build a newer fresher website with the new name. I will need a concept of the home page and one inside page. You can see our current site at https://www.harborsignalnetworks.example and the new site will be https://www.crewbeacon.example .

I also really like the https://www.pathlantern.example/ website. I like ledgerkite.example website. I like the https://skillorbit.example/ website.

See the attached document for layout and some text to use. Use the pictures I attached as opposed to pictures from the old site as much as you can.

Target Market(s)

Business

Industry/Entity Type

Software Service

Number of Pages Required

2 page

Font styles to use
Sans Serif

Requirements
Must have
• Use the colors from my logo. Professional but modern. We want people to feel like our product makes their staff feel safer at work.
Should not have
• Don't use any red or orange (no stop colors).

```html
<!DOCTYPE html>
<html lang="en">
<head>
<meta charset="utf-8">
<title>CrewBeacon – Feel Confident that your Staff is protected</title>
<link href="https://fonts.googleapis.com/css2?family=Poppins:wght@300;400;500;600;700;800&family=Great+Vibes&display=swap" rel="stylesheet">
<style>
:root{
  --blue:#3a97d4;
  --green:#7ab648;
  --navy:#34495e;
  --ink:#3b4250;
  --muted:#5f6672;
  --line:#e6e9ee;
  --white:#ffffff;
}
*{margin:0;padding:0;box-sizing:border-box}
html,body{width:1200px;height:4323px;overflow:hidden}
body{position:relative;font-family:'Poppins',sans-serif;color:var(--ink);background:var(--white)}
.abs{position:absolute}
.btn{position:absolute;display:flex;align-items:center;justify-content:center;background:var(--green);color:#fff;font-size:11px;font-weight:500;letter-spacing:.3px;text-transform:uppercase;border-radius:3px;box-shadow:0 4px 10px rgba(0,0,0,.12)}
.brand{display:flex;align-items:center;gap:10px;font-weight:600;color:var(--navy);font-size:26px}
.brand .dot{width:40px;height:40px;border-radius:50%;background:var(--blue)}

/* header */
.site-header{position:absolute;left:0;top:0;width:1200px;height:91px;background:#fff}
.site-header .brand{position:absolute;left:80px;top:24px}
.nav a{position:absolute;top:38px;font-size:12px;color:var(--ink);text-decoration:none}
.search{position:absolute;left:888px;top:36px}
.login{left:945px;top:32px;width:170px;height:38px;font-size:11px;gap:8px}

/* hero */
.hero{position:absolute;left:0;top:91px;width:1200px;height:521px;background:linear-gradient(100deg,#1d3f63 0%,#2b5e8a 45%,#4d86ad 75%,#2d5b80 100%)}
.hero h1{position:absolute;left:82px;top:110px;width:420px;font-size:43px;line-height:46px;font-weight:800;color:#fff}
.hero p{position:absolute;left:82px;top:275px;width:400px;font-size:22px;line-height:30px;color:#fff;font-weight:400}
.hero .btn{left:85px;top:374px;width:250px;height:50px}
.video{position:absolute;left:495px;top:90px;width:615px;height:352px;background:linear-gradient(180deg,#2a2e33,#3a3f45 60%,#2b2f34);}
.video .bar{position:absolute;left:0;bottom:0;width:100%;height:34px;display:flex;align-items:center;padding:0 14px;gap:12px;color:#fff;font-size:10px}
.video .track{flex:1;height:5px;background:#9aa0a6;border-radius:3px;position:relative}
.video .track::before{content:"";position:absolute;left:0;top:-3px;width:11px;height:11px;border-radius:50%;background:#fff}
.video .vol{width:60px;height:5px;background:#fff;border-radius:3px}

/* features */
.feature{position:absolute;top:692px;width:320px;height:260px;border-radius:8px;overflow:hidden;box-shadow:0 4px 12px rgba(0,0,0,.12)}
.feature .photo{height:208px}
.feature .band{height:52px;display:flex;align-items:center;justify-content:center;color:#fff;font-size:20px;font-weight:600}
.feature-text{position:absolute;top:983px;width:320px;text-align:center;font-size:13px;line-height:26px;color:var(--muted)}

/* dividers */
.divider{position:absolute;left:107px;width:966px;height:1px;background:var(--line)}
.divider-mark{position:absolute;left:578px;width:44px;height:44px;border-radius:50%;background:var(--blue);border:6px solid #fff;box-shadow:0 0 0 1px var(--line)}

.section-title{position:absolute;left:0;width:1200px;text-align:center;font-weight:700;color:var(--navy);font-size:49px;line-height:62px;letter-spacing:.3px}
.lead{position:absolute;left:0;width:1200px;text-align:center;font-size:14px;line-height:27px;color:var(--ink)}

.map{position:absolute;background:radial-gradient(ellipse at center,#eef0f3 0%,#f5f6f8 55%,rgba(255,255,255,0) 75%)}

/* shields */
.shield{position:absolute;top:1870px;width:360px;height:430px}
.shield svg{position:absolute;left:0;top:0}
.shield .copy{position:absolute;left:60px;top:110px;width:230px;text-align:center}
.shield h3{font-size:17px;font-weight:500;color:var(--ink);line-height:24px;margin-bottom:16px}
.shield p{font-size:12px;line-height:26px;color:var(--ink)}
.checks{display:grid;grid-template-columns:1fr 1fr;gap:0 10px;text-align:left;margin:10px auto 0;width:160px}
.checks span{font-size:11.5px;line-height:34px;border-bottom:1px solid #eee;white-space:nowrap}
.checks span::before{content:"✓";color:var(--green);margin-right:6px}

/* stats band */
.stats{position:absolute;left:0;top:2543px;width:1200px;height:212px;background:linear-gradient(90deg,#2b3a4a 0%,#4b5a68 35%,#6f7a80 55%,#5a7a5a 80%,#3e5e44 100%)}
.stats .note{position:absolute;left:103px;top:29px;width:397px;height:140px;background:var(--blue);color:#fff;font-size:23px;line-height:31px;padding:23px 30px}
.stat{position:absolute;top:42px;width:128px;height:128px;border-radius:50%;background:#3b4a58;border:4px solid #fff;color:#fff;text-align:center}
.stat b{display:block;font-size:56px;font-weight:700;line-height:60px;margin-top:20px}
.stat i{font-size:15px}
.covering{position:absolute;left:770px;top:55px;font-family:'Great Vibes',cursive;color:#fff;font-size:66px;line-height:80px}

/* steps */
.step{position:absolute;top:3030px;width:310px;height:380px}
.step svg{position:absolute;left:0;top:0}
.step h4{position:absolute;left:0;width:310px;text-align:center;color:#fff;font-weight:600;font-size:16px;line-height:24px}
.step .list{position:absolute;left:70px;top:205px;width:170px}
.step .list span{display:block;font-size:11.5px;line-height:42px;border-bottom:1px solid #eee}
.step .list span::before{content:"✓";color:var(--blue);margin-right:8px}
.step .grid{position:absolute;left:60px;top:205px;width:190px;display:grid;grid-template-columns:1fr 1fr;gap:0 14px}
.step .grid span{font-size:11.5px;line-height:42px;border-bottom:1px solid #eee}
.step .grid span::before{content:"✓";color:var(--blue);margin-right:8px}
.step p{position:absolute;left:60px;top:210px;width:190px;text-align:center;font-size:11.5px;line-height:26px}

/* footer */
.site-footer{position:absolute;left:0;top:3714px;width:1200px;height:609px;border-top:4px solid var(--green);background:#fff}
.call-label{position:absolute;left:112px;top:96px;font-size:13px;color:var(--blue)}
.phone{position:absolute;left:112px;top:116px;font-size:21px;font-weight:500;color:var(--ink)}
.about{position:absolute;left:112px;top:180px;width:300px;font-size:13.5px;line-height:26px;color:var(--ink)}
.fcol{position:absolute;top:100px}
.fcol h5{font-size:19px;font-weight:500;color:var(--navy);margin-bottom:20px}
.fcol a{display:block;font-size:14px;line-height:38.6px;color:var(--ink);text-decoration:none}
.fcol a::before{content:"✓";color:var(--blue);margin-right:12px}
.footer-rule{position:absolute;left:112px;top:477px;width:976px;height:1px;background:var(--line)}
.site-footer .brand{position:absolute;left:115px;top:515px}
.copyright{position:absolute;left:938px;top:538px;font-size:13px;color:var(--ink)}
</style>
</head>
<body>

<header class="site-header">
  <div class="brand"><span class="dot"></span>CrewBeacon</div>
  <nav class="nav">
    <a style="left:708px">Home</a>
    <a style="left:778px">Buy Addons</a>
  </nav>
  <svg class="search" width="20" height="20" viewBox="0 0 20 20"><circle cx="8" cy="8" r="6" fill="none" stroke="#3b4250" stroke-width="1.6"/><line x1="12.5" y1="12.5" x2="18" y2="18" stroke="#3b4250" stroke-width="1.6"/></svg>
  <a class="btn login"><svg width="14" height="14" viewBox="0 0 14 14"><circle cx="7" cy="4.5" r="3" fill="none" stroke="#fff" stroke-width="1.3"/><path d="M1.5 13c0-3 2.5-4.5 5.5-4.5s5.5 1.5 5.5 4.5" fill="none" stroke="#fff" stroke-width="1.3"/></svg>Customer Login</a>
</header>

<section class="hero" role="img" aria-label="Photo of a hand pulling a panic button from a jeans pocket">
  <h1>Feel Confident that your Staff is protected</h1>
  <p>Get a revolutionary new electronic panic button</p>
  <a class="btn">Ready to get started</a>
  <div class="video" role="img" aria-label="Video still of a person wearing a panic button on a lanyard">
    <div class="bar">
      <svg width="12" height="12" viewBox="0 0 12 12"><path d="M2 1l9 5-9 5z" fill="#fff"/></svg>
      <div class="track"></div>
      <span>00:00</span>
      <svg width="14" height="12" viewBox="0 0 14 12"><path d="M1 4h3l4-3v10l-4-3H1z" fill="#fff"/><path d="M10 3q2 3 0 6" stroke="#fff" fill="none"/></svg>
      <div class="vol"></div>
      <svg width="14" height="12" viewBox="0 0 14 12"><rect x="1" y="1" width="12" height="10" fill="none" stroke="#fff" stroke-width="1.4"/></svg>
    </div>
  </div>
</section>

<div class="feature" style="left:91px;border:2px solid var(--blue)">
  <div class="photo" role="img" aria-label="Hand holding a panic button near a pocket" style="background:linear-gradient(160deg,#2c4f74,#6d8aa3)"></div>
  <div class="band" style="background:var(--blue)">Problems Stopped</div>
</div>
<div class="feature" style="left:432px;border:2px solid var(--green)">
  <div class="photo" role="img" aria-label="Hand pressing a desk mounted panic button" style="background:linear-gradient(160deg,#3a3f45,#b9bec2)"></div>
  <div class="band" style="background:var(--green)">Affordable Prices</div>
</div>
<div class="feature" style="left:776px;border:2px solid var(--navy)">
  <div class="photo" role="img" aria-label="Office desk phone beside a panic button" style="background:linear-gradient(160deg,#4a5560,#c9ced2)"></div>
  <div class="band" style="background:var(--navy)">Many Choices</div>
</div>
<p class="feature-text" style="left:91px">Problems Stopped Before They Start<br>For Any Type Of Organization</p>
<p class="feature-text" style="left:440px">Affordable Prices Starting at $18 per<br>month. No Contracts. No Hidden<br>Costs.</p>
<p class="feature-text" style="left:776px">Alerts by computer, mobile device,<br>text, phone, email, monitoring and E911</p>

<div class="divider" style="top:1148px"></div>
<div class="divider-mark" style="top:1126px"></div>

<h2 class="section-title" style="top:1240px">YOUR EMPOYEES SHOULDN’T<br>FEEL ALONE WHEN THEY NEED HELP</h2>
<p class="lead" style="top:1391px">Does this problem make you feel frustrated and anxious?<br>Put a simple solution in their hands</p>
<a class="btn" style="left:475px;top:1486px;width:250px;height:50px">Ready to get started</a>

<div class="divider" style="top:1628px"></div>
<div class="divider-mark" style="top:1606px"></div>

<h2 class="section-title" style="top:1740px">WHY BUSINESSES CHOOSE US</h2>
<div class="map" role="img" aria-label="Faint world map" style="left:60px;top:1850px;width:1080px;height:520px"></div>

<div class="shield" style="left:62px">
  <svg width="360" height="430" viewBox="0 0 360 430">
    <path d="M170 10 L12 100 L12 240 Q20 330 170 410 Q320 330 328 240 L328 100 Z" fill="var(--blue)" transform="translate(22,-12)"/>
    <path d="M170 10 L12 100 L12 240 Q20 330 170 410 Q320 330 328 240 L328 100 Z" fill="#fff" style="filter:drop-shadow(0 6px 10px rgba(0,0,0,.15))"/>
    <path d="M170 28 L26 110 L26 238 Q34 320 170 392 Q306 320 314 238 L314 110 Z" fill="none" stroke="var(--blue)" stroke-width="1.5" stroke-dasharray="7 6"/>
  </svg>
  <div class="copy"><h3 style="margin-top:40px">Easy to use</h3><p>Press a button and let the right people know you need help and open a chat window letting everyone talk on resolving their problem.</p></div>
</div>
<div class="shield" style="left:428px">
  <svg width="360" height="430" viewBox="0 0 360 430">
    <path d="M170 10 L12 100 L12 240 Q20 330 170 410 Q320 330 328 240 L328 100 Z" fill="var(--green)" transform="translate(22,-12)"/>
    <path d="M170 10 L12 100 L12 240 Q20 330 170 410 Q320 330 328 240 L328 100 Z" fill="#fff" style="filter:drop-shadow(0 6px 10px rgba(0,0,0,.15))"/>
    <path d="M170 28 L26 110 L26 238 Q34 320 170 392 Q306 320 314 238 L314 110 Z" fill="none" stroke="var(--green)" stroke-width="1.5" stroke-dasharray="7 6"/>
  </svg>
  <div class="copy" style="top:100px"><h3 style="margin-bottom:10px">Communicate the<br>way you want</h3><p>We give you lots of options:</p>
    <div class="checks"><span>Computer</span><span>Text</span><span>Mobile</span><span>E911</span><span>Email</span><span>Call Center</span><span>Phone call</span></div>
  </div>
</div>
<div class="shield" style="left:795px">
  <svg width="360" height="430" viewBox="0 0 360 430">
    <path d="M170 10 L12 100 L12 240 Q20 330 170 410 Q320 330 328 240 L328 100 Z" fill="var(--navy)" transform="translate(22,-12)"/>
    <path d="M170 10 L12 100 L12 240 Q20 330 170 410 Q320 330 328 240 L328 100 Z" fill="#fff" style="filter:drop-shadow(0 6px 10px rgba(0,0,0,.15))"/>
    <path d="M170 28 L26 110 L26 238 Q34 320 170 392 Q306 320 314 238 L314 110 Z" fill="none" stroke="var(--navy)" stroke-width="1.5" stroke-dasharray="7 6"/>
  </svg>
  <div class="copy" style="top:105px"><h3>Cost Effective<br>Protection</h3><p>By leveraging your existing network and equipment we can lower your costs to give better options to your staff.</p></div>
</div>
<a class="btn" style="left:475px;top:2372px;width:250px;height:50px">Ready to get started</a>

<section class="stats" role="img" aria-label="Photo of a hand reaching for a panic button under a desk">
  <div class="note">That’s why we have provided a way for customers to get help to staff effectively in</div>
  <div class="stat" style="left:624px"><b>45</b><i>states</i></div>
  <div class="covering">Covering</div>
  <div class="stat" style="left:968px"><b>5</b><i>countries</i></div>
</section>

<h2 class="section-title" style="top:2872px">SIMPLE START PLAN</h2>
<div class="map" role="img" aria-label="Faint world map" style="left:90px;top:2990px;width:1020px;height:480px"></div>

<div class="step" style="left:98px">
  <svg width="310" height="380" viewBox="0 0 310 380">
    <defs><clipPath id="c1"><circle cx="155" cy="230" r="148"/></clipPath></defs>
    <circle cx="155" cy="230" r="148" fill="#fff" style="filter:drop-shadow(0 6px 10px rgba(0,0,0,.12))"/>
    <rect x="0" y="80" width="310" height="100" fill="var(--blue)" clip-path="url(#c1)"/>
    <path d="M10 180 h16 l-8 12z M284 180 h16 l-8 12z" fill="#2a3340"/>
    <circle cx="155" cy="230" r="132" fill="none" stroke="var(--blue)" stroke-width="1.5" stroke-dasharray="7 6" clip-path="inset(0 0 0 0)" stroke-dashoffset="0" transform="" style="clip-path:inset(52% 0 0 0)"/>
    <path d="M115 12 L155 0 L195 12 L195 60 Q190 92 155 108 Q120 92 115 60 Z" fill="#1f2328" stroke="#fff" stroke-width="4"/>
    <text x="155" y="72" text-anchor="middle" fill="#fff" font-family="Poppins,sans-serif" font-size="42" font-weight="700">1</text>
  </svg>
  <h4 style="top:132px">Explore Your Choices</h4>
  <div class="grid"><span>Pricing</span><span>Quote</span><span>Trial</span><span>Hardware</span></div>
</div>
<div class="step" style="left:431px">
  <svg width="310" height="380" viewBox="0 0 310 380">
    <defs><clipPath id="c2"><circle cx="155" cy="230" r="148"/></clipPath></defs>
    <circle cx="155" cy="230" r="148" fill="#fff" style="filter:drop-shadow(0 6px 10px rgba(0,0,0,.12))"/>
    <rect x="0" y="80" width="310" height="100" fill="var(--green)" clip-path="url(#c2)"/>
    <path d="M10 180 h16 l-8 12z M284 180 h16 l-8 12z" fill="#2a3340"/>
    <circle cx="155" cy="230" r="132" fill="none" stroke="var(--green)" stroke-width="1.5" stroke-dasharray="7 6" style="clip-path:inset(52% 0 0 0)"/>
    <path d="M115 12 L155 0 L195 12 L195 60 Q190 92 155 108 Q120 92 115 60 Z" fill="#1f2328" stroke="#fff" stroke-width="4"/>
    <text x="155" y="72" text-anchor="middle" fill="#fff" font-family="Poppins,sans-serif" font-size="42" font-weight="700">2</text>
  </svg>
  <h4 style="top:132px">Get Setup</h4>
  <div class="list" style="left:75px;width:165px"><span>Input Your Alerts</span><span>Input Your Staff</span><span>Install Our Software</span></div>
</div>
<div class="step" style="left:764px">
  <svg width="310" height="380" viewBox="0 0 310 380">
    <defs><clipPath id="c3"><circle cx="155" cy="230" r="148"/></clipPath></defs>
    <circle cx="155" cy="230" r="148" fill="#fff" style="filter:drop-shadow(0 6px 10px rgba(0,0,0,.12))"/>
    <rect x="0" y="80" width="310" height="100" fill="var(--navy)" clip-path="url(#c3)"/>
    <path d="M10 180 h16 l-8 12z M284 180 h16 l-8 12z" fill="#2a3340"/>
    <circle cx="155" cy="230" r="132" fill="none" stroke="var(--navy)" stroke-width="1.5" stroke-dasharray="7 6" style="clip-path:inset(52% 0 0 0)"/>
    <path d="M115 12 L155 0 L195 12 L195 60 Q190 92 155 108 Q120 92 115 60 Z" fill="#1f2328" stroke="#fff" stroke-width="4"/>
    <text x="155" y="72" text-anchor="middle" fill="#fff" font-family="Poppins,sans-serif" font-size="42" font-weight="700">3</text>
  </svg>
  <h4 style="top:120px">Feel Confident Your<br>Staff Is Protected</h4>
  <p>High Five. You just too a major step to getting rid of the anxiety and frustration this gave you.</p>
</div>
<a class="btn" style="left:475px;top:3535px;width:250px;height:50px">Start my demo</a>

<footer class="site-footer">
  <span class="call-label">Call Us</span>
  <span class="phone">1 – 800 – 555 – 0148</span>
  <p class="about">When employees feel alone during a threatening situation, we give them a way to let the right resources know that they need help so you can feel confident that your staff is protected.</p>
  <div class="fcol" style="left:483px"><h5>SHOP</h5><a>Add Ons</a><a>Start My Demo</a><a>Custom Quote</a><a>Start Trial</a></div>
  <div class="fcol" style="left:684px"><h5>ABOUT</h5><a>Affiliates</a><a>Contact</a><a>Support</a><a>Existing Customers</a><a>Industries</a><a>Blog</a><a>FAQ</a></div>
  <div class="fcol" style="left:900px"><h5>LEGAL</h5><a>Privacy Policy</a><a>Terms of Use</a><a>End User License</a><a>Agreement</a></div>
  <div class="footer-rule"></div>
  <div class="brand"><span class="dot"></span>CrewBeacon</div>
  <span class="copyright">©CrewBeacon 2020</span>
</footer>

</body>
</html>
```